Zolvix Activewear business card design

I need a business card designed for my activewear business. I would like to use the colours pink, purple white and blue. please see attached logo. please include (name) Harriet Lomberg (phone) 0417862035 (email) hattiezolvix@mailbox.example (ABN) 48193570264 . please include - Free shipping on all orders over $100

Target Market(s)

female

Contact Information for Business Card

Colors

Designer to choose colors to be used in the design.

Requirements
Must have
• I need a business card designed for my activewear business. I would like to use the colours pink, purple white and blue. please see attached logo. please include (name) Harriet Lomberg (phone) 0417862035 (email) hattiezolvix@mailbox.example (ABN) 48193570264 . please include - Free shipping on all orders over $100

```html
<!DOCTYPE html>
<html lang="en">
<head>
<meta charset="utf-8">
<title>Zolvix Activewear — Business Card</title>
<link rel="stylesheet" href="https://fonts.googleapis.com/css2?family=Raleway:wght@300;400;700&family=Open+Sans:wght@400;600;700&display=swap">
<style>
  :root {
    --backdrop: #8b8b8d;
    --card-white: #ffffff;
    --card-fade: #e4e4e6;
    --ink-dark: #1f1d20;
    --brand-purple: #8e2b8f;
    --brand-magenta: #a3218f;
    --lavender-start: #9b5ba1;
    --lavender-end: #b37db8;
    --text-light: #f2f2f2;
    --label-purple: #a04aa0;
  }
  * { margin: 0; padding: 0; box-sizing: border-box; }
  html, body { width: 1200px; height: 1176px; overflow: hidden; }
  body { background: var(--backdrop); position: relative; font-family: "Open Sans", sans-serif; }

  .card {
    position: absolute; left: 200px; width: 782px; border-radius: 28px; overflow: hidden;
    box-shadow: 0 10px 22px rgba(0,0,0,0.35);
  }
  .card--front {
    top: 90px; height: 448px;
    background: linear-gradient(180deg, var(--card-fade) 0%, var(--card-white) 40%, var(--card-white) 100%);
  }
  .card--back { top: 600px; height: 445px; background: var(--ink-dark); }

  .brand-name {
    position: absolute; font-family: "Raleway", sans-serif; font-weight: 700;
    color: var(--brand-purple); letter-spacing: 2px; white-space: nowrap;
  }
  .card--front .brand-name { left: 0; right: 0; top: 78px; text-align: center; font-size: 44px; }
  .card--back .brand-name { left: 0; right: 0; top: 190px; text-align: center; font-size: 54px; }

  .accent-rule { position: absolute; left: 0; right: 0; top: 200px; height: 6px; background: var(--brand-magenta); }
  .info-band { position: absolute; left: 0; right: 0; top: 210px; height: 172px; background: var(--ink-dark); }

  .holder { position: absolute; right: 419px; top: 54px; text-align: right; font-family: "Raleway", sans-serif; }
  .holder__name { color: var(--text-light); font-size: 26px; font-weight: 300; letter-spacing: 0.5px; white-space: nowrap; }
  .holder__name strong { font-weight: 700; }
  .holder__title { color: var(--label-purple); font-size: 18px; font-weight: 400; margin-top: 4px; }

  .divider { position: absolute; left: 390px; top: 13px; width: 2px; height: 142px; background: var(--brand-magenta); }

  .contacts { position: absolute; left: 408px; top: 36px; list-style: none; }
  .contacts li { display: flex; align-items: center; height: 33px; color: var(--text-light); font-size: 18.5px; }
  .contacts .icon { width: 38px; display: flex; align-items: center; padding-left: 10px; }
  .contacts .label { width: 50px; color: var(--label-purple); font-size: 17px; padding-left: 1px; }
  .contacts .value { margin-left: 12px; }
  .contacts li:last-child .value { margin-left: 0; }

  .promo-band {
    position: absolute; left: 0; right: 0; top: 388px; height: 30px;
    background: linear-gradient(90deg, var(--lavender-start), var(--lavender-end));
    color: var(--text-light); font-size: 18.5px; text-align: center; line-height: 30px;
  }
  .promo-band strong { font-weight: 700; }
</style>
</head>
<body>
  <section class="card card--front">
    <div class="brand-name">ZOLVIX</div>
    <div class="accent-rule"></div>
    <div class="info-band">
      <div class="holder">
        <div class="holder__name">HARRIET <strong>LOMBERG</strong></div>
        <div class="holder__title">JOB TITLE</div>
      </div>
      <div class="divider"></div>
      <ul class="contacts">
        <li>
          <span class="icon"><svg width="18" height="14" viewBox="0 0 18 14"><path d="M1 5 Q9 -1 17 5 L15 7 L12 5 L12 3 Q9 2 6 3 L6 5 L3 7 Z" fill="#a3218f"/><rect x="4" y="7" width="10" height="7" rx="1" fill="#a3218f"/></svg></span>
          <span class="value">0417862035</span>
        </li>
        <li>
          <span class="icon"><svg width="17" height="12" viewBox="0 0 17 12"><rect width="17" height="12" fill="#a3218f"/><path d="M0 0 L8.5 7 L17 0" fill="none" stroke="#1f1d20" stroke-width="1.4"/></svg></span>
          <span class="value">hattiezolvix@mailbox.example</span>
        </li>
        <li>
          <span class="label">ABN</span>
          <span class="value">48193570264</span>
        </li>
      </ul>
    </div>
    <div class="promo-band">Free shipping on all orders over <strong>$100</strong></div>
  </section>

  <section class="card card--back">
    <div class="brand-name">ZOLVIX</div>
  </section>
</body>
</html>
```